Business Card

i would like to have a professional HD business card in PSD file
be creative

the company called ( Bright Pixel Works )
our services is web development and marketing
My Name is Karim Saleh
Title: Regional Manager ( Middle East )
Phone Number section
Email Section
Address section
Website: [url removed, login to view]

```html
<!DOCTYPE html>
<html lang="en">
<head>
<meta charset="UTF-8">
<title>Bright Pixel Works – Business Card</title>
<link href="https://fonts.googleapis.com/css2?family=Roboto:wght@400;500;700&display=swap" rel="stylesheet">
<style>
  :root {
    --backdrop: #2f3337;
    --card: #ffffff;
    --accent: #ee8a2c;
    --ink: #1f2333;
    --shadow: rgba(0, 0, 0, 0.35);
  }
  * { margin: 0; padding: 0; box-sizing: border-box; }
  html, body {
    width: 1200px;
    height: 900px;
    overflow: hidden;
    background: var(--backdrop);
    font-family: "Roboto", Arial, sans-serif;
  }
  .canvas {
    position: relative;
    width: 1200px;
    height: 900px;
  }
  .card {
    position: absolute;
    width: 560px;
    height: 320px;
    background: var(--card);
    border-radius: 22px;
    box-shadow: 0 14px 30px var(--shadow);
    color: var(--accent);
  }
  /* Brand side */
  .card--brand {
    left: 580px;
    top: 90px;
  }
  .brand-block {
    position: absolute;
    left: 70px;
    top: 56px;
  }
  .brand-mark {
    width: 120px;
    height: 96px;
    background: var(--ink);
    margin-left: 120px;
    margin-bottom: 22px;
  }
  .brand-name {
    font-weight: 700;
    font-size: 38px;
    line-height: 1.1;
    color: var(--accent);
  }
  .brand-tagline {
    margin-top: 14px;
    font-weight: 500;
    font-size: 22px;
    letter-spacing: 0.5px;
    text-transform: uppercase;
    color: var(--accent);
  }
  /* Contact side */
  .card--contact {
    left: 60px;
    top: 490px;
  }
  .person {
    position: absolute;
    left: 36px;
    top: 34px;
  }
  .person-name {
    font-weight: 700;
    font-size: 28px;
  }
  .person-title {
    margin-top: 4px;
    font-size: 14px;
  }
  .contact-list {
    position: absolute;
    left: 36px;
    top: 176px;
    list-style: none;
  }
  .contact-item {
    display: flex;
    align-items: center;
    gap: 10px;
    font-size: 15px;
    line-height: 26px;
  }
  .contact-icon {
    width: 14px;
    height: 14px;
    fill: var(--accent);
    flex: none;
  }
  .contact-brand {
    position: absolute;
    right: 36px;
    top: 140px;
    text-align: right;
  }
  .contact-brand .brand-mark {
    width: 96px;
    height: 76px;
    margin: 0 0 14px auto;
  }
  .contact-brand .brand-name {
    font-size: 30px;
  }
</style>
</head>
<body>
<main class="canvas">

  <section class="card card--brand">
    <div class="brand-block">
      <div class="brand-mark" aria-hidden="true"></div>
      <p class="brand-name">Bright Pixel Works</p>
      <p class="brand-tagline">Web Development and Marketing</p>
    </div>
  </section>

  <section class="card card--contact">
    <div class="person">
      <p class="person-name">Karim Saleh</p>
      <p class="person-title">Regional Manager ( Middle East )</p>
    </div>

    <ul class="contact-list">
      <li class="contact-item">
        <svg class="contact-icon" viewBox="0 0 24 24" aria-hidden="true"><path d="M6.6 10.8a15.1 15.1 0 0 0 6.6 6.6l2.2-2.2c.3-.3.7-.4 1-.2 1.1.4 2.3.6 3.6.6.6 0 1 .4 1 1V20c0 .6-.4 1-1 1C10.6 21 3 13.4 3 4c0-.6.4-1 1-1h3.5c.6 0 1 .4 1 1 0 1.3.2 2.5.6 3.6.1.3 0 .7-.2 1z"/></svg>
        <span>+000 12 345 6789</span>
      </li>
      <li class="contact-item">
        <svg class="contact-icon" viewBox="0 0 24 24" aria-hidden="true"><path d="M2 5h20v14H2z M2 5l10 8 10-8" /></svg>
        <span>info@brightpixel.com</span>
      </li>
      <li class="contact-item">
        <svg class="contact-icon" viewBox="0 0 24 24" aria-hidden="true"><path d="M12 3 2 12h3v8h5v-5h4v5h5v-8h3z"/></svg>
        <span>address here</span>
      </li>
      <li class="contact-item">
        <svg class="contact-icon" viewBox="0 0 24 24" aria-hidden="true"><circle cx="12" cy="12" r="10"/></svg>
        <span>www.BrightPixelWorks.com</span>
      </li>
    </ul>

    <div class="contact-brand">
      <div class="brand-mark" aria-hidden="true"></div>
      <p class="brand-name">Bright Pixel Works</p>
    </div>
  </section>

</main>
</body>
</html>
```